Business Cards for Tech Company - uBrightowl

We would like new modern business cards designed for our company. Attached are some examples of other business cards we like. <br/><br/>Info we need is: <br/>First Name, Last Name<br/>Address<br/>Store Phone<br/>Cell Phone<br/>Email Address<br/>Text Logo <br/>And Other Logo<br/>

Industry/Entity Type

Technology Equipment

Contact Information for Business Card

Please use these details as example:

Dale Morrow
Technology Specialist
Direct 555.617.2094
Phone 555-730-8186

dale.morrow@ubrightowl.example

2971 Willet Lane
Larkfield, ND 00427

Font styles to use
Sans Serif
Other font styles liked:
• Anything easy to read and modern

Colors

Designer to choose colors to be used in the design.

Requirements
Must have
• Both Logos
• Signature as name
• Use the text logo and use the shark logo but do not use the full shark logo. Have it where it is zoomed in and is expanding out of the card.
Nice to have
• Keep it clean and modern
• We like blue, white, and black/grays.
Should not have
• Random icons for phone and address.

```html
<!DOCTYPE html>
<html lang="en">
<head>
<meta charset="utf-8">
<title>uBrightowl Business Card</title>
<link rel="stylesheet" href="https://fonts.googleapis.com/css2?family=Open+Sans:wght@400;600;800&display=swap">
<style>
  :root {
    --brand-blue: #1473cf;
    --ink: #1c1c1c;
    --logo-gray: #5f6061;
    --band-gray: #a7a8aa;
    --paper: #ffffff;
    --backdrop: #e6e7e9;
  }
  * { box-sizing: border-box; margin: 0; padding: 0; }
  html, body {
    width: 1200px; height: 977px; overflow: hidden;
    background: var(--backdrop);
    font-family: "Open Sans", Arial, sans-serif;
  }
  .canvas { position: relative; width: 1200px; height: 977px; }
  .card {
    position: absolute; left: 250px; width: 700px; height: 400px;
    overflow: hidden; box-shadow: 0 6px 18px rgba(0,0,0,.18);
  }
  .card-back {
    top: 60px; background: var(--brand-blue);
    display: flex; align-items: center; justify-content: center;
  }
  .card-back .wordmark { color: var(--paper); font-size: 72px; }
  .wordmark { font-weight: 800; letter-spacing: -1px; line-height: 1; }

  .card-front { top: 517px; background: var(--paper); }
  .card-front .wordmark {
    position: absolute; left: 58px; top: 82px;
    color: var(--logo-gray); font-size: 52px;
  }
  .holder { position: absolute; right: 70px; top: 92px; text-align: right; }
  .holder-name { color: var(--brand-blue); font-size: 22px; font-weight: 600; letter-spacing: .5px; }
  .holder-title { color: var(--ink); font-size: 13px; margin-top: 2px; }
  .rule-thin {
    position: absolute; left: 60px; top: 212px; width: 410px; height: 1px; background: var(--ink);
  }
  .rule-blue {
    position: absolute; left: 470px; top: 211px; width: 162px; height: 3px; background: var(--brand-blue);
  }
  .address {
    position: absolute; right: 46px; top: 226px; text-align: right;
    color: var(--ink); font-size: 12.5px; line-height: 17px; font-style: normal;
  }
  .contacts { position: absolute; left: 62px; top: 248px; list-style: none; }
  .contacts li {
    display: flex; align-items: center; gap: 9px;
    color: var(--ink); font-size: 13.5px; line-height: 24px;
  }
  .contacts svg { width: 12px; height: 12px; flex: none; }
  .icon-phone { fill: var(--brand-blue); }
  .icon-mail { fill: var(--brand-blue); }
  .icon-mail .flap { fill: none; stroke: var(--paper); stroke-width: 2; }
  .band { position: absolute; bottom: 0; height: 34px; }
  .band-blue { left: 0; width: 590px; background: var(--brand-blue); }
  .band-gray { left: 608px; right: 0; background: var(--band-gray); }
</style>
</head>
<body>
<main class="canvas">
  <section class="card card-back" aria-label="Card back">
    <span class="wordmark">uBrightowl</span>
  </section>

  <section class="card card-front" aria-label="Card front">
    <span class="wordmark">uBrightowl</span>
    <div class="holder">
      <div class="holder-name">Dale Morrow</div>
      <div class="holder-title">Technology Specialist</div>
    </div>
    <div class="rule-thin"></div>
    <div class="rule-blue"></div>
    <address class="address">2971 Willet Lane<br>Larkfield, ND 00427</address>
    <ul class="contacts">
      <li><svg class="icon-phone" viewBox="0 0 24 24"><path d="M6.6 10.8a15.1 15.1 0 0 0 6.6 6.6l2.2-2.2a1 1 0 0 1 1-.25 11.4 11.4 0 0 0 3.6.57 1 1 0 0 1 1 1V20a1 1 0 0 1-1 1A17 17 0 0 1 3 4a1 1 0 0 1 1-1h3.5a1 1 0 0 1 1 1c0 1.25.2 2.45.57 3.57a1 1 0 0 1-.25 1z"/></svg>555.617.2094(Direct)</li>
      <li><svg class="icon-phone" viewBox="0 0 24 24"><path d="M6.6 10.8a15.1 15.1 0 0 0 6.6 6.6l2.2-2.2a1 1 0 0 1 1-.25 11.4 11.4 0 0 0 3.6.57 1 1 0 0 1 1 1V20a1 1 0 0 1-1 1A17 17 0 0 1 3 4a1 1 0 0 1 1-1h3.5a1 1 0 0 1 1 1c0 1.25.2 2.45.57 3.57a1 1 0 0 1-.25 1z"/></svg>555-730-8186</li>
      <li><svg class="icon-mail" viewBox="0 0 24 24"><rect x="2" y="5" width="20" height="14"/><path class="flap" d="M2 6l10 7 10-7"/></svg>dale.morrow@ubrightowl.example</li>
    </ul>
    <div class="band band-blue"></div>
    <div class="band band-gray"></div>
  </section>
</main>
</body>
</html>
```